Trailbound Hub Outfitter Directory

Hero Section
Image: A serene and picturesque camping landscape with a lake, mountains, and a few trees There is a circle of people sitting around a campfire. The image should be high-quality and visually appealing.
Headline: "Introducing Trailboundhub.com's Outfitter Directory"
Subheading: "Join our directory of trusted outfitters and reach a targeted audience of camping enthusiasts."
Call-to-Action (CTA) Button: "Learn More" or "Join Now"
Color scheme: Match trailboundhub.com and the logo
Example:
[Image: A serene and picturesque camping landscape with a lake, mountains, and a few trees]
Introducing Trailboundhub.com's Outfitter Directory
Join our directory of trusted outfitters and reach a targeted audience of camping enthusiasts.
Learn More
Benefits Section
Image: A group of happy campers sitting around a campfire, roasting marshmallows and telling stories.
Headline: "Benefits of Joining Our Directory"
Bullet points:
"Increase your exposure and visibility to potential customers"
"Book more trips and generate more revenue"
"Access a targeted audience of camping enthusiasts"
Color scheme: match trailboundhub.com
Example:
[Image: A group of happy campers sitting around a campfire, roasting marshmallows and telling stories]
Benefits of Joining Our Directory
• Increase your exposure and visibility to potential customers • Book more trips and generate more revenue • Access a targeted audience of camping enthusiasts
Features Section
Image: A screenshot of the directory's search functionality, showing a list of outfitters with their logos, names, and locations.
Headline: "Features of Our Outfitter Directory"
Bullet points:
"Search functionality to find outfitters by location, activity, or type"
"Outfitter profiles with detailed information and reviews"
"Booking system to make it easy for customers to book trips"
Example:
[Image: A screenshot of the directory's search functionality, showing a list of outfitters with their logos, names, and locations]
Features of Our Outfitter Directory
• Search functionality to find outfitters by location, activity, or type • Outfitter profiles with detailed information and reviews • Booking system to make it easy for customers to book trips
CTA Section
Image: A simple and clean design with a prominent call-to-action button.
Headline: "Express Interest in Joining Our Directory"
Call-to-Action (CTA) Button: "Express Interest" or "Join Now"

Example:
[Image: A simple and clean design with a prominent call-to-action button]
Express Interest in Joining Our Directory
Express Interest
Contact Information Section
Image: A simple and clean design with a form to collect contact information.
Headline: "Get in Touch with Us"
Form fields:
Name
Email
Phone
Website

```html
<!DOCTYPE html>
<html lang="en">
<head>
<meta charset="utf-8">
<title>Trailbound Hub – Outfitter Directory</title>
<link rel="stylesheet" href="https://fonts.googleapis.com/css2?family=Bebas+Neue&family=Montserrat:ital,wght@0,400;0,500;0,600;0,700;1,400&family=Gochi+Hand&display=swap">
<style>
:root{
  --navy:#0f2747;
  --orange:#ee3b12;
  --ink:#3b3f48;
  --muted:#8a8f99;
  --panel:#f3f4f7;
  --white:#ffffff;
  --line:#c9ccd2;
  --teal:#1d8fa6;
}
*{margin:0;padding:0;box-sizing:border-box}
html,body{width:1200px;height:4115px;overflow:hidden}
body{font-family:"Montserrat",sans-serif;color:var(--ink);background:var(--white);position:relative}
section,header,footer{position:relative;width:1200px}
.abs{position:absolute}
.display{font-family:"Bebas Neue",sans-serif;color:var(--navy);font-weight:400;letter-spacing:1px}
.btn{position:absolute;background:var(--orange);color:var(--white);font-size:12px;font-weight:700;letter-spacing:1px;display:flex;align-items:center;justify-content:center;text-transform:uppercase}
.brand{display:flex;align-items:center;gap:8px;font-family:"Bebas Neue",sans-serif;color:var(--white);font-size:24px;line-height:1}
.brand-dot{width:22px;height:22px;border-radius:50%;background:var(--orange);flex:none}

/* Hero */
.hero{height:636px;background:linear-gradient(180deg,#6d5a4a 0%,#b8865a 22%,#7c5a3f 40%,#3a2c22 70%,#1e1914 100%)}
.hero-shade{inset:0;background:rgba(0,0,0,.18)}
.hero .brand{left:140px;top:38px}
.contact-chip{display:flex;align-items:center;gap:10px;color:var(--white);top:34px}
.chip-icon{width:32px;height:32px;border-radius:50%;background:var(--orange);display:flex;align-items:center;justify-content:center}
.chip-text small{display:block;font-size:9px;opacity:.9}
.chip-text span{font-size:10px;font-weight:500}
.hero-divider{left:1021px;top:30px;width:1px;height:40px;background:rgba(255,255,255,.6)}
.hero-tagline{left:0;width:1200px;top:150px;text-align:center;font-family:"Gochi Hand",cursive;color:var(--white);font-size:32px}
.hero-title{left:0;width:1200px;top:190px;text-align:center;color:var(--white);font-family:"Bebas Neue",sans-serif;font-weight:400;font-size:86px;line-height:86px;letter-spacing:3px}
.hero-sub{left:0;width:1200px;top:374px;text-align:center;color:var(--white);font-size:13px;font-weight:500}

/* About */
.about{height:690px}
.about-ghost{left:172px;top:70px;font-family:"Gochi Hand",cursive;font-size:76px;color:transparent;-webkit-text-stroke:1.5px #d4d6db;letter-spacing:6px;line-height:64px}
.about-photo{left:141px;top:131px;width:445px;height:395px;background:linear-gradient(180deg,#8fa7a4 0%,#4f6b55 35%,#6f8b8d 60%,#a56f72 80%,#7b7a78 100%)}
.about-panel{left:588px;top:70px;width:470px;height:516px;background:var(--panel);padding:74px 24px 0 41px}
.about-panel h2{font-size:46px;line-height:46px;margin-bottom:16px}
.about-panel h3{font-family:"Bebas Neue",sans-serif;color:var(--navy);font-size:24px;font-weight:400;margin:20px 0 6px;letter-spacing:.5px}
.about-panel p{font-size:12.5px;line-height:23px;text-align:justify}
.about-badge{left:1003px;top:514px;width:107px;height:107px;border-radius:50%;background:var(--white);border:3px solid var(--navy);display:flex;align-items:center;justify-content:center;text-align:center;font-family:"Bebas Neue",sans-serif;color:var(--navy);font-size:20px;line-height:20px}

/* Benefits */
.benefits{height:707px;background:var(--panel)}
.benefits-photo{left:610px;top:0;width:590px;height:707px;background:linear-gradient(180deg,#8ec3e6 0%,#b9d8ea 25%,#9a8a6c 55%,#6f6454 80%,#a9a398 100%)}
.benefits h2{left:66px;top:62px;font-size:50px;line-height:50px;width:480px}
.benefit{left:67px;width:486px;height:107px;background:var(--white);border-radius:54px;box-shadow:0 4px 14px rgba(0,0,0,.06);display:flex;align-items:center;padding-left:9px}
.benefit-icon{width:92px;height:92px;border-radius:50%;background:var(--orange);display:flex;align-items:center;justify-content:center;flex:none}
.benefit-text{font-family:"Bebas Neue",sans-serif;color:var(--navy);font-size:21px;line-height:27px;letter-spacing:.5px;margin-left:20px}

/* Products */
.products{height:383px}
.products h2{left:0;width:1200px;top:62px;text-align:center;font-size:50px}
.product{width:160px;text-align:center;top:142px}
.product-circle{width:140px;height:140px;border-radius:50%;background:var(--white);box-shadow:0 4px 16px rgba(0,0,0,.08);margin:0 auto;display:flex;align-items:center;justify-content:center}
.product-label{font-family:"Bebas Neue",sans-serif;color:var(--navy);font-size:18px;margin-top:24px;letter-spacing:.5px}

/* CTA banner */
.banner{height:388px;background:linear-gradient(90deg,#2d3a2e 0%,#4d5b3f 25%,#3d4336 50%,#2b2f2a 75%,#3a3a34 100%)}
.banner h2{left:692px;top:66px;color:var(--white);font-size:50px;line-height:59px;letter-spacing:2px}

/* Testimonials */
.testimonials{height:496px}
.testimonials h2{left:0;width:1200px;top:62px;text-align:center;font-size:50px}
.side-card{top:210px;width:117px;height:150px;background:var(--white);box-shadow:0 2px 10px rgba(0,0,0,.04);font-size:8px;font-style:italic;color:#c4c6cb;display:flex;align-items:center;overflow:hidden;white-space:nowrap}
.quote-card{left:275px;top:178px;width:649px;height:206px;background:var(--white);box-shadow:0 4px 18px rgba(0,0,0,.07);text-align:center}
.avatar{left:564px;top:141px;width:70px;height:70px;border-radius:50%;background:linear-gradient(180deg,#c9b9a8,#8b6d55);border:3px solid var(--white)}
.stars{left:0;width:100%;top:58px;color:#f6b400;font-size:13px;letter-spacing:2px}
.quote-title{left:0;width:100%;top:80px;font-size:13px;font-weight:600;color:var(--navy)}
.quote-body{left:0;width:100%;top:110px;font-size:11.5px;font-style:italic}
.quote-name{left:0;width:100%;top:152px;font-family:"Bebas Neue",sans-serif;color:var(--navy);font-size:14px;letter-spacing:.5px}
.arrow{top:266px;width:28px;height:28px;border-radius:50%;display:flex;align-items:center;justify-content:center}
.dots{left:0;width:1200px;top:412px;display:flex;justify-content:center;gap:7px;align-items:center}
.dots i{width:7px;height:7px;border-radius:50%;background:#dadce0;display:block}
.dots i.on{width:11px;height:11px;background:var(--orange)}

/* Contact */
.contact{height:564px}
.contact-photo{left:0;top:0;width:599px;height:564px;background:linear-gradient(180deg,#4e6a3a 0%,#6f7f45 30%,#4a4a3b 60%,#8a5a2a 85%,#3b3128 100%)}
.contact h2{left:670px;top:92px;font-size:50px}
.contact-intro{left:670px;top:160px;width:400px;font-size:12px;line-height:23px}
.field{height:36px;border-bottom:1px solid var(--line);font-size:10px;color:var(--muted);padding:10px 0 0 12px}

/* Footer */
.site-footer{height:251px;background:var(--panel)}
.site-footer .brand{left:141px;top:88px;color:var(--navy);font-size:28px}
.foot-item{top:88px;display:flex;align-items:center;gap:14px}
.foot-icon{width:40px;height:40px;border-radius:50%;background:var(--orange);display:flex;align-items:center;justify-content:center}
.foot-item strong{display:block;font-size:11px;color:var(--navy);font-weight:600}
.foot-item span{font-size:11px}
.foot-rule{left:141px;top:196px;width:918px;height:1px;background:#dfe1e5}
.copyright{left:141px;top:216px;font-size:10px}
.socials{left:928px;top:210px;display:flex;gap:10px}
.socials i{display:block;width:25px;height:25px;border-radius:50%;background:var(--orange)}
</style>
</head>
<body>

<header class="hero">
  <div class="abs hero-shade" role="img" aria-label="Hiker with raised arms on a ridge above a tent at sunset in the mountains"></div>
  <div class="abs brand"><span class="brand-dot"></span>Trailbound Hub</div>
  <div class="abs contact-chip" style="left:645px">
    <span class="chip-icon"><svg width="14" height="14" viewBox="0 0 24 24" fill="#fff"><path d="M2 5h20v14H2z"/><path d="M2 5l10 8 10-8" stroke="#ee3b12" stroke-width="2" fill="none"/></svg></span>
    <span class="chip-text"><small>Email Us</small><span>info@trailboundhub.com</span></span>
  </div>
  <div class="abs contact-chip" style="left:866px">
    <span class="chip-icon"><svg width="14" height="14" viewBox="0 0 24 24" fill="#fff"><path d="M6.6 10.8a15 15 0 006.6 6.6l2.2-2.2a1 1 0 011-.25 11.4 11.4 0 003.6.6 1 1 0 011 1V20a1 1 0 01-1 1A17 17 0 013 4a1 1 0 011-1h3.5a1 1 0 011 1c0 1.250.2 2.45.6 3.6a1 1 0 01-.25 1z"/></svg></span>
    <span class="chip-text"><small>Call Anytime</small><span>(555) 214-7730</span></span>
  </div>
  <div class="abs hero-divider"></div>
  <svg class="abs" style="left:1042px;top:40px" width="18" height="18" viewBox="0 0 24 24" fill="none" stroke="#fff" stroke-width="2"><circle cx="10" cy="10" r="6"/><path d="M15 15l5 5"/></svg>
  <div class="abs hero-tagline">Fun For The Whole Family</div>
  <h1 class="abs hero-title">Camping With<br>Family Gives Joy</h1>
  <p class="abs hero-sub">Join our directory of trusted outfitters and reach a targeted audience of camping enthusiasts.</p>
  <a class="btn" style="left:524px;top:423px;width:150px;height:40px">Join Now</a>
</header>

<section class="about">
  <div class="abs about-ghost">ABOUT US</div>
  <div class="abs about-photo" role="img" aria-label="Smiling man with outstretched arms standing in front of a mountain lake and pine forest"></div>
  <div class="abs about-panel">
    <h2 class="display">Who We Are</h2>
    <p>Here at Trailbound Hub, we love exploring just as much as you do. We have all the best gear to make your adventures possible.</p>
    <h3>Our Mission</h3>
    <p>We are committed to being there for our customers wherever your adventures should take you.</p>
    <h3>Our Vision</h3>
    <p>We carefully select manufacturers that embody our core values of providing the highest quality products with the lowest carbon footprint. We only get one earth to live on, so we must protect it.</p>
  </div>
  <div class="abs about-badge">Trailbound<br>Hub</div>
</section>

<section class="benefits">
  <h2 class="abs display">Benefits of Joining Our Directory</h2>
  <div class="abs benefit" style="top:192px">
    <span class="benefit-icon"><svg width="44" height="44" viewBox="0 0 44 44" fill="none" stroke="#fff" stroke-width="1.6"><circle cx="22" cy="13" r="5"/><path d="M14 30a8 8 0 0116 0z"/><circle cx="10" cy="21" r="3.5"/><circle cx="34" cy="21" r="3.5"/><path d="M4 34a6 6 0 0112 0M28 34a6 6 0 0112 0"/></svg></span>
    <span class="benefit-text">Increase your exposure and visibility<br>to potential customers</span>
  </div>
  <div class="abs benefit" style="top:325px">
    <span class="benefit-icon"><svg width="44" height="44" viewBox="0 0 44 44" fill="none" stroke="#fff" stroke-width="1.6"><circle cx="11" cy="11" r="6"/><path d="M11 8v6M9 9.5h3.5"/><rect x="8" y="28" width="5" height="10"/><rect x="17" y="23" width="5" height="15"/><rect x="26" y="18" width="5" height="20"/><rect x="35" y="14" width="5" height="24"/><path d="M18 16l8-6 6 4 8-8M36 6h4v4"/></svg></span>
    <span class="benefit-text">Book more trips and generate<br>more revenue</span>
  </div>
  <div class="abs benefit" style="top:453px">
    <span class="benefit-icon"><svg width="44" height="44" viewBox="0 0 44 44" fill="none" stroke="#fff" stroke-width="1.6"><circle cx="22" cy="22" r="15"/><circle cx="22" cy="22" r="10"/><circle cx="22" cy="19" r="3.5"/><path d="M16 28a6 6 0 0112 0"/><path d="M22 3v4M22 37v4M3 22h4M37 22h4"/></svg></span>
    <span class="benefit-text">Access a targeted audience of camping<br>enthusiasts</span>
  </div>
  <a class="btn" style="left:67px;top:596px;width:150px;height:40px">Join Now</a>
  <div class="abs benefits-photo" role="img" aria-label="Laughing young woman with a yellow backpack hiking on a rocky mountain top"></div>
</section>

<section class="products">
  <h2 class="abs display">Our Products</h2>
  <div class="abs product" style="left:88px">
    <div class="product-circle"><svg width="76" height="60" viewBox="0 0 76 60" fill="none" stroke="#0f2747" stroke-width="2.2"><path d="M10 6l-6 16M10 6l6 16M66 6l-6 16M66 6l6 16M4 22h12M60 22h12M10 22c8 30 48 30 56 0M16 26c10 16 34 16 44 0"/><path d="M8 52h60"/></svg></div>
    <div class="product-label">Hammocks</div>
  </div>
  <div class="abs product" style="left:260px">
    <div class="product-circle"><svg width="60" height="66" viewBox="0 0 60 66" fill="none" stroke="#0f2747" stroke-width="2.2"><rect x="20" y="4" width="20" height="10" rx="4"/><rect x="10" y="14" width="40" height="48" rx="10"/><rect x="18" y="34" width="24" height="16" rx="3"/><path d="M4 30v24M56 30v24M18 40h24"/></svg></div>
    <div class="product-label">Backpacks</div>
  </div>
  <div class="abs product" style="left:433px">
    <div class="product-circle"><svg width="70" height="66" viewBox="0 0 70 66" fill="none" stroke="#0f2747" stroke-width="2.2"><path d="M22 8v12M30 14v6M38 10v10M16 20h38v6H16zM22 26l18 28M48 26L30 54M8 38h14v8H8zM48 38h14v8H48zM10 46l-4 14M20 46l4 14M50 46l-4 14M60 46l4 14M18 58h34"/></svg></div>
    <div class="product-label">Camp Furniture</div>
  </div>
  <div class="abs product" style="left:606px">
    <div class="product-circle"><svg width="76" height="66" viewBox="0 0 76 66" fill="none" stroke="#0f2747" stroke-width="2.2"><path d="M20 4c-2 3 2 5 0 8M28 4c-2 3 2 5 0 8M36 4c-2 3 2 5 0 8M12 18h32v12H12zM44 22h14M8 30h42v16H8zM50 36h20v8H50z"/><circle cx="18" cy="38" r="4"/><path d="M14 46l-4 16M44 46l4 16M26 38h16"/></svg></div>
    <div class="product-label">Camp Kitchen</div>
  </div>
  <div class="abs product" style="left:778px">
    <div class="product-circle"><svg width="66" height="62" viewBox="0 0 66 62" fill="none" stroke="#0f2747" stroke-width="2.2"><rect x="6" y="6" width="54" height="50" rx="6"/><path d="M6 22h54M14 12h38"/><rect x="14" y="30" width="38" height="18" rx="2"/><rect x="24" y="42" width="18" height="6"/></svg></div>
    <div class="product-label">Coolers</div>
  </div>
  <div class="abs product" style="left:951px">
    <div class="product-circle"><svg width="72" height="66" viewBox="0 0 72 66" fill="none" stroke="#0f2747" stroke-width="2.2"><rect x="26" y="4" width="20" height="12"/><path d="M26 10h20M36 4v12M36 16v8M36 24L8 58h56zM36 24v34M2 58h68"/><rect x="14" y="44" width="8" height="8"/><rect x="48" y="44" width="8" height="8"/></svg></div>
    <div class="product-label">Electronics</div>
  </div>
</section>

<section class="banner" role="img" aria-label="Glowing green tent beside a mountain lake at dusk with pine trees">
  <h2 class="abs display">Get Now Memorable<br>Wonderful Outdoor<br>Experiences</h2>
  <a class="btn" style="left:693px;top:269px;width:151px;height:40px">Join Now</a>
</section>

<section class="testimonials">
  <h2 class="abs display">What Our Clients Say</h2>
  <div class="abs side-card" style="left:147px;justify-content:flex-end;padding-right:2px">Hands down best</div>
  <div class="abs side-card" style="left:935px;padding-left:2px">ce is just as good</div>
  <div class="abs quote-card">
    <div class="abs stars">★★★★★</div>
    <div class="abs quote-title">Trailbound Hub!</div>
    <div class="abs quote-body">Hands down best prices I've found online and their customer service is just as good.</div>
    <div class="abs quote-name">Daniel R.</div>
  </div>
  <div class="abs avatar" role="img" aria-label="Customer portrait"></div>
  <span class="abs arrow" style="left:261px;background:var(--navy)"><svg width="10" height="10" viewBox="0 0 10 10" fill="none" stroke="#fff" stroke-width="2"><path d="M6.5 1.5L3 5l3.5 3.5"/></svg></span>
  <span class="abs arrow" style="left:910px;background:var(--orange)"><svg width="10" height="10" viewBox="0 0 10 10" fill="none" stroke="#fff" stroke-width="2"><path d="M3.5 1.5L7 5 3.5 8.5"/></svg></span>
  <div class="abs dots"><i></i><i></i><i class="on"></i><i></i><i></i></div>
</section>

<section class="contact">
  <div class="abs contact-photo" role="img" aria-label="Young couple crouching by a campfire in front of a green tent in a pine forest"></div>
  <h2 class="abs display">Get In Touch</h2>
  <p class="abs contact-intro">We will try our best to help you. Please fill up the form with the correct detail and we'll be in touch asap.</p>
  <div class="abs field" style="left:670px;top:218px;width:193px">Full Name*</div>
  <div class="abs field" style="left:880px;top:218px;width:194px">Phone*</div>
  <div class="abs field" style="left:670px;top:276px;width:193px">Email*</div>
  <div class="abs field" style="left:880px;top:276px;width:194px">Website*</div>
  <div class="abs field" style="left:670px;top:332px;width:388px;height:56px">Message</div>
  <a class="btn" style="left:670px;top:423px;width:116px;height:42px">Submit</a>
</section>

<footer class="site-footer">
  <div class="abs brand"><span class="brand-dot"></span>Trailbound Hub</div>
  <div class="abs foot-item" style="left:387px">
    <span class="foot-icon"><svg width="18" height="18" viewBox="0 0 24 24" fill="none" stroke="#fff" stroke-width="2.2"><circle cx="12" cy="12" r="9"/><path d="M12 7v5l3 2"/></svg></span>
    <div><strong>Timing</strong><span>Mon-Fri - 10AM-7PM ET</span></div>
  </div>
  <div class="abs foot-item" style="left:630px">
    <span class="foot-icon"><svg width="16" height="16" viewBox="0 0 24 24" fill="#fff"><path d="M6.6 10.8a15 15 0 006.6 6.6l2.2-2.2a1 1 0 011-.25 11.4 11.4 0 003.6.6 1 1 0 011 1V20a1 1 0 01-1 1A17 17 0 013 4a1 1 0 011-1h3.5a1 1 0 011 1c0 1.25.2 2.45.6 3.6a1 1 0 01-.25 1z"/></svg></span>
    <div><strong>Call Anytime</strong><span style="color:var(--teal);font-size:14px;font-weight:600">(555) 214-7730</span></div>
  </div>
  <div class="abs foot-item" style="left:848px">
    <span class="foot-icon"><svg width="16" height="16" viewBox="0 0 24 24" fill="#fff"><path d="M2 5h20v14H2z"/><path d="M2 5l10 8 10-8" stroke="#ee3b12" stroke-width="2" fill="none"/></svg></span>
    <div><strong>Email</strong><span>info@trailboundhub.com</span></div>
  </div>
  <div class="abs foot-rule"></div>
  <div class="abs copyright">© 2024 Trailbound Hub. All Rights Reserved.</div>
  <div class="abs socials"><i></i><i></i><i></i><i></i></div>
</footer>

</body>
</html>
```